KestrelNet Business Cards

Create business cards for our exciting new software company. We provide cloud billing systems and provisioning software for campany that need monthly SaaS and Cloud Billing

Target Market(s)

Enterprise businesses, b2b, telecom carriers, software manufactures

Industry/Entity Type

Software

```html
<!DOCTYPE html>
<html lang="en">
<head>
<meta charset="utf-8">
<title>KestrelNet Business Cards</title>
<link href="https://fonts.googleapis.com/css2?family=Tenor+Sans&family=Josefin+Sans:wght@400;600&display=swap" rel="stylesheet">
<style>
  :root {
    --backdrop: #c7d1d6;
    --card-white: #ffffff;
    --card-navy: #1c3a5c;
    --ink-grey: #6b6b6b;
    --ink-navy: #1f3d60;
    --sky: #8ccbec;
    --sky-soft: #d6ecf8;
  }
  * { margin: 0; padding: 0; box-sizing: border-box; }
  html, body { width: 1200px; height: 960px; overflow: hidden; }
  body {
    background: var(--backdrop);
    position: relative;
    font-family: "Tenor Sans", "Josefin Sans", sans-serif;
  }
  .card {
    position: absolute;
    left: 250px;
    width: 700px;
    height: 400px;
    box-shadow: 0 10px 30px rgba(20, 40, 60, 0.25);
    overflow: hidden;
  }
  .card-front { top: 60px; background: var(--card-white); }
  .card-back { top: 500px; background: var(--card-navy); }

  .corner-glow {
    position: absolute;
    right: 0;
    bottom: 0;
    width: 260px;
    height: 240px;
    background: radial-gradient(ellipse at 100% 100%, var(--sky-soft) 0%, rgba(214,236,248,0) 70%);
  }

  .holder-name {
    position: absolute;
    left: 45px;
    top: 78px;
    font-size: 36px;
    letter-spacing: 2px;
    color: var(--ink-grey);
    text-transform: uppercase;
  }
  .holder-role {
    position: absolute;
    left: 47px;
    top: 122px;
    font-size: 24px;
    letter-spacing: 3px;
    color: var(--ink-grey);
    text-transform: uppercase;
  }
  .contact-list {
    position: absolute;
    left: 47px;
    top: 190px;
    list-style: none;
    color: var(--ink-grey);
  }
  .contact-list li {
    display: flex;
    align-items: center;
    gap: 14px;
    height: 32px;
    font-size: 21px;
    letter-spacing: 1.5px;
  }
  .contact-list .email { font-size: 16px; text-transform: uppercase; letter-spacing: 2px; }
  .contact-list svg { width: 18px; height: 18px; flex: none; }

  .address {
    position: absolute;
    left: 47px;
    top: 290px;
    font-size: 21px;
    line-height: 30px;
    letter-spacing: 1.5px;
    color: var(--ink-grey);
    font-style: normal;
  }
  .website {
    position: absolute;
    left: 47px;
    top: 356px;
    font-family: "Josefin Sans", sans-serif;
    font-weight: 600;
    font-size: 17px;
    letter-spacing: 2.5px;
    color: var(--ink-navy);
    text-transform: uppercase;
  }

  .brand {
    position: absolute;
    text-align: right;
  }
  .brand-name {
    display: block;
    font-size: 36px;
    letter-spacing: 0.5px;
  }
  .brand-tagline {
    display: block;
    font-size: 8.5px;
    line-height: 11px;
    letter-spacing: 1.2px;
    text-transform: uppercase;
    margin-top: 4px;
  }
  .card-front .brand { right: 40px; top: 62px; color: var(--ink-navy); }
  .card-front .brand-tagline { color: var(--ink-grey); }
  .card-back .brand { right: 60px; top: 150px; color: var(--sky); }
  .card-back .brand-name { font-size: 44px; }
  .card-back .brand-tagline { color: var(--sky); font-size: 10px; line-height: 13px; }
</style>
</head>
<body>

  <section class="card card-front" aria-label="Business card front">
    <div class="corner-glow"></div>

    <h1 class="holder-name">Dana Whitfield</h1>
    <p class="holder-role">PPC Specialist</p>

    <ul class="contact-list">
      <li>
        <svg viewBox="0 0 18 18" aria-hidden="true">
          <rect x="1.5" y="2" width="15" height="14" rx="1.5" fill="none" stroke="#1f3d60" stroke-width="1.6"/>
          <rect x="4" y="4.5" width="3" height="9" fill="#1f3d60"/>
          <rect x="9" y="5" width="5" height="2" fill="#1f3d60"/>
          <rect x="9" y="9" width="2" height="2" fill="#1f3d60"/>
          <rect x="12" y="9" width="2" height="2" fill="#1f3d60"/>
          <rect x="9" y="12" width="2" height="2" fill="#1f3d60"/>
          <rect x="12" y="12" width="2" height="2" fill="#1f3d60"/>
        </svg>
        <span>(954) 555-0142</span>
      </li>
      <li>
        <svg viewBox="0 0 18 18" aria-hidden="true">
          <rect x="1.5" y="3.5" width="15" height="11" fill="none" stroke="#1f3d60" stroke-width="1.6"/>
          <path d="M1.5 3.5 L16.5 14.5 M16.5 3.5 L1.5 14.5" stroke="#1f3d60" stroke-width="1.4"/>
        </svg>
        <span class="email">dana@kestrelnet.com</span>
      </li>
    </ul>

    <address class="address">418 Coral Way,<br>Fort Lauderdale, FL 33304</address>
    <p class="website">www.kestrelnet.com</p>

    <div class="brand">
      <span class="brand-name">KestrelNet</span>
      <span class="brand-tagline">Cloud billing and<br>operational support systems</span>
    </div>
  </section>

  <section class="card card-back" aria-label="Business card back">
    <div class="brand">
      <span class="brand-name">KestrelNet</span>
      <span class="brand-tagline">Cloud billing and<br>operational support systems</span>
    </div>
  </section>

</body>
</html>
```